Postcard Design for Thank Yous

I am a Voice Actor and want to send personal thank you cards or postcards to clients after recording sessions. the basic concept is front art that simply has background art & my logo (sample below but wrong size), and the other side would be space for mailing address as well as a small version of my logo and contact info and of course plenty of blank space for me to write a personal message. I am open to your opinion as to whether a postcard, or a card and mailing envelope makes more sense. (I am also including the back of business card as example of contact listing, but one number will not be included and I might want to change other verbiage). Thank you! -Neil

```html
<!DOCTYPE html>
<html lang="en">
<head>
<meta charset="utf-8">
<title>Neil Halvorsen – Thank You Postcard</title>
<link rel="stylesheet" href="https://fonts.googleapis.com/css2?family=Pinyon+Script&family=Arimo:wght@400;700&display=swap">
<style>
  :root {
    --page-bg: #e6e6e6;
    --ink-black: #0d0d0d;
    --brand-red: #e8222b;
    --photo-dark: #1e1e1e;
    --photo-mid: #5a5a5a;
    --photo-light: #8a8a8a;
    --paper: #f7f7f8;
    --line-grey: #555555;
    --crowd-tint: #ebecee;
    --white: #ffffff;
  }
  * { box-sizing: border-box; margin: 0; padding: 0; }
  html, body {
    width: 833px; height: 1200px; overflow: hidden;
    background: var(--page-bg);
    font-family: "Arimo", Arial, sans-serif;
  }
  .postcard { position: absolute; left: 101px; width: 631px; overflow: hidden; }

  /* Front */
  .postcard--front { top: 71px; height: 488px; }
  .front__photo {
    position: absolute; inset: 0;
    background: radial-gradient(ellipse at 60% 45%, var(--photo-light) 0%, var(--photo-mid) 38%, var(--photo-dark) 100%);
  }
  .front__photo-strip {
    position: absolute; left: 0; top: 0; width: 154px; height: 100%;
    background: linear-gradient(180deg, #3a3a3a 0%, #2a2a2a 60%, #444 100%);
  }

  /* Shared structure */
  .divider-line {
    position: absolute; left: 152px; top: 0; width: 3px; height: 100%;
    background: var(--brand-red);
  }
  .red-band {
    position: absolute; left: 0; right: 0;
    background: var(--brand-red);
  }
  .brand-mark {
    position: absolute; left: 42px; width: 108px; height: 97px;
    background: var(--brand-red);
    border: 1px solid #333;
    display: flex; align-items: center; justify-content: center;
  }
  .brand-mark__name {
    font-family: "Arimo", Arial, sans-serif;
    font-weight: 700; font-size: 17px; color: var(--ink-black);
  }

  .front__band { top: 202px; height: 83px; }
  .front__mark { top: 198px; }
  .thank-you {
    position: absolute; left: 155px; right: 0; top: 202px; height: 83px;
    display: flex; align-items: center; justify-content: center;
    font-family: "Pinyon Script", cursive;
    font-size: 66px; color: var(--white); line-height: 1;
    padding-left: 10px;
  }

  /* Back */
  .postcard--back { top: 621px; height: 486px; background: var(--paper); }
  .back__header {
    position: absolute; left: 0; top: 0; width: 100%; height: 251px;
    background: var(--ink-black);
  }
  .back__band { top: 79px; height: 52px; }
  .back__mark { top: 70px; }
  .back__identity {
    position: absolute; left: 155px; right: 0; top: 79px; height: 52px;
    text-align: center; color: var(--white);
  }
  .identity__name { font-size: 25px; line-height: 28px; padding-top: 6px; }
  .identity__web { font-size: 18px; line-height: 20px; }
  .contact-list {
    position: absolute; left: 155px; right: 0; top: 167px;
    list-style: none; text-align: center; color: var(--white);
    font-size: 14px; line-height: 18.5px;
  }
  .back__crowd {
    position: absolute; left: 0; right: 0; top: 251px; bottom: 0;
    background: linear-gradient(180deg, var(--paper) 0%, var(--crowd-tint) 45%, var(--paper) 100%);
  }
  .address-lines { position: absolute; left: 40px; top: 330px; width: 263px; }
  .address-line {
    position: absolute; left: 0; width: 100%; height: 1px; background: var(--line-grey);
  }
  .stamp-box {
    position: absolute; left: 461px; top: 338px; width: 120px; height: 115px;
    border: 1px solid #222; background: transparent;
  }
</style>
</head>
<body>

<section class="postcard postcard--front">
  <div class="front__photo" role="img" aria-label="Black and white photo of a card table with poker chips, playing cards and a glass"></div>
  <div class="front__photo-strip" role="img" aria-label="Darker side panel of stacked poker chips"></div>
  <div class="divider-line"></div>
  <div class="red-band front__band"></div>
  <div class="brand-mark front__mark"><span class="brand-mark__name">Halvorsen</span></div>
  <h1 class="thank-you">Thank You</h1>
</section>

<section class="postcard postcard--back">
  <div class="back__header"></div>
  <div class="divider-line" style="height:251px"></div>
  <div class="red-band back__band"></div>
  <div class="brand-mark back__mark"><span class="brand-mark__name">Halvorsen</span></div>
  <div class="back__identity">
    <p class="identity__name">Neil Halvorsen - Voice Actor</p>
    <p class="identity__web">www.neilhalvorsenvoice.com</p>
  </div>
  <ul class="contact-list">
    <li>555.214.3080(office)</li>
    <li>555.371.6642(cell)</li>
    <li>555.408.9157(studio phone patch)</li>
    <li>neil@neilhalvorsenvoice.com</li>
  </ul>
  <div class="back__crowd" role="img" aria-label="Faint silhouette of a cheering crowd"></div>
  <div class="address-lines">
    <span class="address-line" style="top:0"></span>
    <span class="address-line" style="top:45px"></span>
    <span class="address-line" style="top:84px"></span>
    <span class="address-line" style="top:121px"></span>
  </div>
  <div class="stamp-box"></div>
</section>

</body>
</html>
```